One slide graphic for website

I am designing a series of sliders for my website http://new.quillhartmedia.example

The slide I am trying to create has the following message:

EVERY company is a media company.
Empower yours now!

Learn More >

The ideas I have had for imagery are an office building with the letters 'Every Company is a Media Company' either shone onto the building or letters on the building roof ledge ect.

Aby ideas you may have to improve on this would be appreciated.

The idea behind the slide is to promote a software application which gives marketing professionals the chance to increase their media coverage. The message also encourages companies to create their own news on a number of platforms as the media landscape has changed so much. Look at the blue heron stunt whereby they generated 10 million views on clipvault using PR alone.

Good luck and I look forward to seeing your ideas.

Martin

```html
<!DOCTYPE html>
<html lang="en">
<head>
<meta charset="utf-8">
<title>Quillhart – Every company is a media company</title>
<link href="https://fonts.googleapis.com/css2?family=Open+Sans:ital,wght@0,300;0,400;0,600;0,700;1,300;1,400;1,700&display=swap" rel="stylesheet">
<style>
  :root {
    --green: #1f8a45;
    --green-dark: #17733a;
    --green-icon: #1f9a55;
    --orange: #f7941d;
    --purple: #7b3f9e;
    --ink: #333333;
    --grey: #666666;
    --social: #555555;
    --white: #ffffff;
    --line: #e4e4e4;
    --hero-top: #8fbfe0;
    --hero-mid: #4f6f90;
    --hero-bottom: #3a4658;
    --caption: rgba(40, 40, 40, 0.7);
  }
  * { box-sizing: border-box; }
  html, body {
    margin: 0;
    width: 1200px;
    height: 849px;
    overflow: hidden;
    background: var(--white);
    font-family: "Open Sans", Arial, sans-serif;
    color: var(--ink);
  }
  .page { position: relative; width: 1200px; height: 849px; overflow: hidden; }

  /* Header */
  .site-header { position: relative; height: 111px; }
  .brand {
    position: absolute; left: 145px; top: 32px;
    display: flex; align-items: center; gap: 10px;
    font-size: 36px; font-weight: 600; color: var(--green);
    letter-spacing: 0.5px; line-height: 1;
  }
  .brand-dot { width: 14px; height: 14px; border-radius: 50%; background: var(--green); }
  .contact {
    position: absolute; right: 164px; top: 18px;
    display: flex; align-items: center; gap: 6px;
    font-size: 18px; color: var(--grey);
  }
  .contact .phone { margin-right: 8px; }
  .social { width: 21px; height: 21px; border-radius: 50%; background: var(--social); }
  .actions { position: absolute; right: 164px; top: 52px; display: flex; gap: 6px; }
  .action {
    display: flex; align-items: center; gap: 6px;
    height: 27px; padding: 0 10px 0 6px; border-radius: 7px;
    color: var(--white); font-size: 15px; font-weight: 700; font-style: italic;
    text-transform: uppercase; text-decoration: none;
  }
  .action svg { width: 18px; height: 18px; }
  .action-demo { background: var(--purple); width: 126px; }
  .action-login { background: var(--orange); width: 87px; }

  /* Navigation */
  .main-nav {
    height: 47px;
    background: linear-gradient(var(--green-dark) 0 4px, var(--green) 4px);
    padding-left: 145px;
  }
  .main-nav ul { list-style: none; margin: 0; padding: 0; display: flex; height: 100%; }
  .main-nav li {
    display: flex; align-items: center; padding: 4px 14px 0;
    border-right: 1px solid rgba(0,0,0,0.15);
    font-size: 12.5px; font-weight: 700; color: var(--white); text-transform: uppercase;
  }
  .main-nav li.active { background: var(--orange); }

  /* Hero */
  .hero { position: relative; height: 415px; overflow: hidden; }
  .hero-photo {
    position: absolute; inset: 0;
    background: linear-gradient(180deg, var(--hero-top) 0%, var(--hero-mid) 55%, var(--hero-bottom) 100%);
  }
  .hero-caption {
    position: absolute; left: 0; top: 251px; width: 900px; height: 86px;
    background: var(--caption);
  }
  .hero-title {
    position: absolute; left: 144px; top: 253px; margin: 0;
    font-size: 32px; font-weight: 400; line-height: 40px; color: var(--white);
    letter-spacing: -0.3px;
  }
  .hero-cta {
    position: absolute; left: 145px; top: 349px;
    width: 185px; height: 50px; border-radius: 25px 10px 25px 10px;
    background: var(--orange); color: #111;
    display: flex; align-items: center; justify-content: center;
    font-size: 22px; text-transform: uppercase; text-decoration: none;
  }

  /* Intro */
  .tagline {
    margin: 14px 0 0; text-align: center;
    font-size: 32px; font-weight: 300; font-style: italic; line-height: 35px; color: var(--ink);
  }

  /* Features */
  .features { position: absolute; left: 147px; top: 690px; display: flex; gap: 11px; }
  .feature {
    width: 217px; height: 200px; text-align: center;
    border-left: 1px solid var(--line); border-right: 1px solid var(--line);
    box-shadow: 0 0 6px rgba(0,0,0,0.05);
  }
  .feature h2 {
    margin: 6px 0 6px; font-size: 23px; font-weight: 400; font-style: italic; color: var(--ink);
  }
  .feature svg { width: 80px; height: 74px; display: block; margin: 0 auto; }
  .feature p {
    margin: 16px 18px 0; font-size: 12.5px; font-style: italic; line-height: 18px; color: var(--grey);
  }
</style>
</head>
<body>
<div class="page">
  <header class="site-header">
    <div class="brand"><span class="brand-dot"></span>QUILLHART</div>
    <div class="contact">
      <span class="phone">t. +44 (0)1632 960418</span>
      <span class="social"></span><span class="social"></span><span class="social"></span>
    </div>
    <div class="actions">
      <a class="action action-demo" href="#">
        <svg viewBox="0 0 18 18"><circle cx="9" cy="9" r="8" fill="#fff"/><path d="M5 9h7M9 5.5 12.5 9 9 12.5" stroke="#7b3f9e" stroke-width="2" fill="none"/></svg>Free Demo</a>
      <a class="action action-login" href="#">
        <svg viewBox="0 0 18 18"><circle cx="9" cy="9" r="8" fill="#fff"/><path d="M5 9h7M9 5.5 12.5 9 9 12.5" stroke="#f7941d" stroke-width="2" fill="none"/></svg>Login</a>
    </div>
  </header>

  <nav class="main-nav">
    <ul>
      <li class="active">Home</li><li>Software</li><li>Industries</li><li>News</li><li>Webinars</li>
      <li>Free Downloads</li><li>Our Story</li><li>Our Values</li><li>Contact Us</li>
    </ul>
  </nav>

  <section class="hero">
    <div class="hero-photo" role="img" aria-label="Photo of a modern office building under a blue sky"></div>
    <div class="hero-caption"></div>
    <h1 class="hero-title">Every company is a media company.<br>Empower Your Now!</h1>
    <a class="hero-cta" href="#">Learn More</a>
  </section>

  <p class="tagline">Fast and easy way to send press releases, manage your<br>news page &amp; nurture your reputation</p>

  <section class="features">
    <article class="feature">
      <h2>Cloud-based</h2>
      <svg viewBox="0 0 80 74"><path d="M20 62a16 16 0 0 1-2-32 22 22 0 0 1 42-4 18 18 0 0 1 4 36z" fill="#1f8a45"/><path d="M40 30 28 44h8v16h8V44h8z" fill="#fff"/></svg>
      <p>Manage your marketing and PR campaigns with easy use tools from any browser.</p>
    </article>
    <article class="feature">
      <h2>Big Database</h2>
      <svg viewBox="0 0 80 74"><g fill="#1f9a55"><ellipse cx="40" cy="12" rx="30" ry="10"/><path d="M10 18c0 6 14 11 30 11s30-5 30-11v12c0 6-14 11-30 11S10 36 10 30z"/><path d="M10 36c0 6 14 11 30 11s30-5 30-11v12c0 6-14 11-30 11S10 54 10 48z"/><path d="M10 54c0 6 14 11 30 11s30-5 30-11v8c0 6-14 11-30 11S10 68 10 62z"/></g></svg>
      <p>Database of 20,000 journalists with the added ability to be able to add your own.</p>
    </article>
    <article class="feature">
      <h2>Secure &amp; Safe</h2>
      <svg viewBox="0 0 80 74"><path d="M4 6h26l6 8h40v58H4z" fill="#1f9a55"/><rect x="31" y="40" width="18" height="15" rx="2" fill="#fff"/><path d="M34 40v-5a6 6 0 0 1 12 0v5" stroke="#fff" stroke-width="3" fill="none"/></svg>
      <p>Daily backups and hosting on Stackharbor dedicated servers keep data safe.</p>
    </article>
    <article class="feature">
      <h2>Save Time</h2>
      <svg viewBox="0 0 80 74"><path d="M40 8a31 31 0 1 1-29 20" stroke="#1f8a45" stroke-width="8" fill="none"/><path d="M40 2 52 9 40 16z" fill="#1f8a45"/><path d="M40 22v17h14" stroke="#1f8a45" stroke-width="6" fill="none"/></svg>
      <p>Quillhart brilliantly wins media coverage and distributes your news far and wide.</p>
    </article>
  </section>
</div>
</body>
</html>
```